Need a new letterhead

Need a new fresh exciting letterhead. Remove the footer...info is outdated.

Target Market(s)

B2B

Industry/Entity Type

Electrical Power

Colors

Designer to choose colors to be used in the design.

Requirements
Must have
• Red and Blue Corvane Systems Logo
Nice to have
• Powering a brighter, cleaner future in footer...reorganize the words?

```html
<!DOCTYPE html>
<html lang="en">
<head>
<meta charset="utf-8">
<title>Corvane Systems Letterhead</title>
<link rel="stylesheet" href="https://fonts.googleapis.com/css2?family=Tinos&family=Open+Sans:wght@400;600;800&display=swap">
<style>
  :root {
    --backdrop: #e8e8e8;
    --paper: #fbfbfb;
    --paper-shade: #f0f0f0;
    --ink: #4a4a4a;
    --brand-red: #e11f2a;
    --brand-blue: #233a80;
    --tagline: #4d4d4d;
    --white: #ffffff;
  }
  * { box-sizing: border-box; margin: 0; padding: 0; }
  html, body {
    width: 1003px; height: 1200px; overflow: hidden;
    background: var(--backdrop);
  }
  .letterhead {
    position: absolute; left: 75px; top: 0;
    width: 852px; height: 1200px;
    background: linear-gradient(170deg, var(--paper) 0%, var(--paper-shade) 100%);
    overflow: hidden;
    font-family: "Tinos", "Times New Roman", serif;
    color: var(--ink);
  }
  .brand-name {
    position: absolute; left: 0; width: 100%; top: 82px;
    text-align: center;
    font-family: "Open Sans", Arial, sans-serif;
    font-weight: 800; font-size: 36px;
    color: var(--brand-red);
    letter-spacing: 0.5px;
  }
  .letter {
    position: absolute; left: 102px; top: 0;
    font-size: 17.3px; line-height: 20.3px;
  }
  .letter > * { position: absolute; left: 0; white-space: nowrap; }
  .sender-city { top: 220px; }
  .date { top: 261px; }
  .recipient { top: 322px; font-style: normal; }
  .recipient .street { padding-left: 9px; }
  .salutation { top: 444px; }
  .body-intro { top: 485px; }
  .body-fit { top: 696px; }
  .body-thanks { top: 757px; }
  .closing { top: 839px; }
  .signature { top: 880px; }
  .signature .name { padding-left: 33px; }

  .footer-bands { position: absolute; left: 0; top: 0; width: 852px; height: 1200px; }
  .footer-text {
    position: absolute; font-family: "Open Sans", Arial, sans-serif;
    color: var(--white); font-size: 10.5px; line-height: 14px; letter-spacing: 0.4px;
  }
  .footer-address { left: 101px; top: 1131px; }
  .footer-phones { left: 314px; top: 1130px; }
  .footer-phones .row { display: flex; align-items: center; gap: 8px; height: 15px; }
  .footer-phones svg { width: 11px; height: 11px; fill: var(--white); }
  .tagline {
    position: absolute; left: 522px; top: 1127px;
    width: 288px; white-space: nowrap;
    font-family: "Open Sans", Arial, sans-serif;
    font-size: 13.5px; letter-spacing: 1.9px;
    font-variant: small-caps; color: var(--tagline);
  }
  .web-address { left: 621px; top: 1167px; font-size: 11px; letter-spacing: 0.6px; }
</style>
</head>
<body>
  <main class="letterhead">
    <div class="brand-name">Corvane Systems</div>

    <section class="letter">
      <p class="sender-city">Westbrook, NY 11408</p>
      <p class="date">June 28, 2007</p>
      <address class="recipient">
        Ms. Helena Marlowe<br>
        John Doe Fellowship<br>
        <span class="street">210 Larch Avenue</span><br>
        New York, NY 10044
      </address>
      <p class="salutation">Dear Ms. Marlowe:</p>
      <p class="body-intro">
        The John Doe Fellowship has always loomed on the horizon for me. Ever since I<br>
        decided to major in history, I have wanted to participate in your program. From the<br>
        research that I have done, I believe that your program provides its participants with<br>
        an extensively detailed look at the history of the world through hands-on<br>
        experience with fossils, artifacts, and other remains that compose the blueprint of<br>
        our existence.&nbsp; I am applying for the John Doe Fellowship because I believe that it<br>
        would benefit me throughout my career and allow me to further understand the<br>
        ideas behind history and how it is constructed.
      </p>
      <p class="body-fit">
        I believe my skills, experience, and goals make me an excellent candidate for your<br>
        program.
      </p>
      <p class="body-thanks">
        Thank you very much for considering me for the John Doe Fellowship. I am<br>
        looking forward to hearing from you.
      </p>
      <p class="closing">Sincerely,</p>
      <p class="signature"><span class="name">Dana</span><br>(555) 014-2288</p>
    </section>

    <svg class="footer-bands" viewBox="0 0 852 1200" aria-hidden="true">
      <polygon points="324,1168 494,1158 852,1158 852,1200 358,1200" fill="var(--brand-red)"/>
      <polygon points="3,1128 461,1128 507,1168 3,1168" fill="var(--brand-blue)"/>
      <polyline points="461,1128 507,1168" stroke="var(--white)" stroke-width="1.2" fill="none"/>
    </svg>

    <div class="footer-text footer-address">418 Calder Street<br>Ridgefield, Ohio 43122</div>
    <div class="footer-text footer-phones">
      <div class="row">
        <svg viewBox="0 0 24 24"><path d="M6.6 10.8c1.4 2.8 3.8 5.2 6.6 6.6l2.2-2.2c.3-.3.7-.4 1-.2 1.1.4 2.3.6 3.6.6.6 0 1 .4 1 1V20c0 .6-.4 1-1 1C10.6 21 3 13.4 3 4c0-.6.4-1 1-1h3.5c.6 0 1 .4 1 1 0 1.3.2 2.5.6 3.6.1.3 0 .7-.2 1z"/></svg>
        <span>800-555-0142</span>
      </div>
      <div class="row">
        <svg viewBox="0 0 24 24"><path d="M6 3h12v5H6zM3 9h18v8h-3v4H6v-4H3zm5 6v4h8v-4z"/></svg>
        <span>800-555-0143</span>
      </div>
    </div>
    <div class="tagline">Powering a brighter, cleaner future</div>
    <div class="footer-text web-address">www.CorvaneSystems.com</div>
  </main>
</body>
</html>
```